Fontaneau Bayou Grillhouse (Owners Card)

Need a classy, but modern business card. I have included a promotional card for the steakhouse. I need one for myself (the owner) that is more professional.

Target Market(s)

General Public

Industry/Entity Type

Food service

Contact Information for Business Card

Name, business address, phone number, email, logo

Font styles to use
Serif
Sans Serif
Decorative
Script

Requirements
Must have
• My name (Darvin Okafor), business address (627 Harlow Avenue), phone number (520) 394-2751, email (Dokaforzp4@mailbrook.net. On the back of the card: Psalms 27 1 The LORD is my light and my salvation— whom shall I fear? The LORD is the stronghold of my life— of whom shall I be afraid? 2 When the wicked advance against me to devour me, it is my enemies and my foes who will stumble and fall. 3 Though an army besiege me, my heart will not fear; though war break out against me, even then I will be confident.
Nice to have
• Something that’s bold, but modern and professional.

```html
<!DOCTYPE html>
<html lang="en">
<head>
<meta charset="utf-8">
<title>Fontaneau Bayou Grillhouse – Owner Business Card</title>
<link rel="stylesheet" href="https://fonts.googleapis.com/css2?family=Montserrat:wght@800&family=Open+Sans:wght@400;600;700&display=swap">
<style>
  :root {
    --stage: #dcc0a3;
    --card-dark: #1b1b1b;
    --card-light: #ffffff;
    --ink: #1d1d1d;
    --ink-light: #f4f4f4;
    --green: #12a43c;
    --yellow: #f6d10f;
    --orange: #f28a13;
    --red: #e5202a;
    --rasta: linear-gradient(90deg, var(--green) 0%, var(--yellow) 40%, var(--orange) 65%, var(--red) 100%);
  }
  * { box-sizing: border-box; margin: 0; padding: 0; }
  html, body { width: 1200px; height: 711px; overflow: hidden; }
  body {
    background: var(--stage);
    font-family: "Open Sans", Arial, sans-serif;
    display: flex;
    align-items: center;
    justify-content: center;
    gap: 40px;
  }
  .card {
    position: relative;
    width: 540px;
    height: 309px;
    box-shadow: 0 12px 28px rgba(60, 35, 15, 0.28);
    overflow: hidden;
  }
  .card::after {
    content: "";
    position: absolute;
    left: 0; right: 0; bottom: 0;
    height: 5px;
    background: var(--rasta);
  }
  .gradient-text {
    background: var(--rasta);
    -webkit-background-clip: text;
    background-clip: text;
    color: transparent;
  }

  /* Brand name block (stands where the mark sits) */
  .brand {
    display: flex;
    align-items: center;
    gap: 10px;
  }
  .brand-dot {
    width: 14px; height: 14px;
    border-radius: 50%;
    background: var(--red);
    flex: none;
  }
  .brand-name {
    font-family: "Open Sans", Arial, sans-serif;
    font-weight: 700;
    font-size: 25px;
    line-height: 1.1;
    color: var(--red);
  }

  /* Back of card */
  .card-back {
    background: var(--card-dark);
    color: var(--ink-light);
    display: grid;
    grid-template-columns: 230px 1fr;
    align-items: center;
    padding: 0 28px 0 34px;
  }
  .card-back .brand-name { color: var(--yellow); }
  .scripture-title {
    font-weight: 600;
    font-size: 13px;
    letter-spacing: 0.5px;
    display: inline-block;
    margin-bottom: 4px;
  }
  .verse {
    display: flex;
    gap: 8px;
    font-size: 11.2px;
    line-height: 1.35;
    margin-bottom: 12px;
  }
  .verse:last-child { margin-bottom: 0; }
  .verse-bullet {
    flex: none;
    width: 8px; height: 8px;
    margin-top: 4px;
    border-radius: 50%;
    background: linear-gradient(90deg, var(--green) 50%, var(--red) 50%);
  }

  /* Front of card */
  .card-front {
    background: var(--card-light);
    color: var(--ink);
    padding: 34px 38px;
  }
  .owner { margin-top: 44px; }
  .owner-name {
    font-family: "Montserrat", Arial, sans-serif;
    font-weight: 800;
    font-size: 30px;
    line-height: 1.05;
    display: inline-block;
  }
  .owner-title { font-weight: 600; font-size: 15px; }
  .contact {
    margin-top: 20px;
    font-size: 12.5px;
    line-height: 1.7;
  }
  .label { font-weight: 700; }
  .label-t { color: var(--red); }
  .label-e { color: var(--orange); }
  .label-w { color: var(--green); }
</style>
</head>
<body>

  <section class="card card-back" aria-label="Card back">
    <div class="brand">
      <span class="brand-dot"></span>
      <span class="brand-name">Fontaneau Bayou Grillhouse</span>
    </div>
    <div class="scripture">
      <span class="scripture-title gradient-text">PSALMS 27</span>
      <p class="verse"><span class="verse-bullet"></span><span>The LORD is my light and my salvation – whom shall I fear? The LORD is the stronghold of my life– of whom shall I be afraid?</span></p>
      <p class="verse"><span class="verse-bullet"></span><span>When the wicked advance against me to devour me, it is my enemies and my foes who will stumble and fall.</span></p>
      <p class="verse"><span class="verse-bullet"></span><span>Though an army besiege me, my heart will not fear; though war break out against me, even then I will be confident.</span></p>
    </div>
  </section>

  <section class="card card-front" aria-label="Card front">
    <div class="brand">
      <span class="brand-dot"></span>
      <span class="brand-name">Fontaneau Bayou Grillhouse</span>
    </div>
    <div class="owner">
      <h1 class="owner-name gradient-text">Darvin Okafor</h1>
      <p class="owner-title">Owner</p>
    </div>
    <div class="contact">
      <p><span class="label label-t">T:</span> (520) 394-2751</p>
      <p>627 Harlow Avenue, Ashbury, CA, United States, California</p>
      <p><span class="label label-e">E:</span> Dokaforzp4@mailbrook.net <span class="label label-w">W:</span> www.fontbayou.com</p>
    </div>
  </section>

</body>
</html>
```